Corvalith business website

I am wanting a website for my media agency Corvalith.

It needs to be be an attractive, unique and professional looking website. The website is a destination for people to be able to understand the service that Corvalith offers.

Please read uploaded website copy to gain an understanding of the business.

Target Market(s)

small business owners, business decision makers, marketing managers,

Industry/Entity Type

Business

Requirements
Must have
• Good branding.

```html
<!DOCTYPE html>
<html lang="en">
<head>
<meta charset="utf-8">
<title>Corvalith – Media Strategy, Planning and Buying</title>
<link rel="stylesheet" href="https://fonts.googleapis.com/css2?family=Source+Sans+3:wght@400;600;700&display=swap">
<style>
  :root {
    --brand-blue: #0000e0;
    --nav-grey: #d2d2d2;
    --nav-stripe: #a9a9a9;
    --text-dark: #333333;
    --text-body: #777777;
    --footer-grey: #c8c8c8;
    --frame-grey: #e2e2e2;
    --white: #ffffff;
  }
  * { box-sizing: border-box; margin: 0; padding: 0; }
  html, body { width: 1200px; height: 812px; overflow: hidden; background: var(--white); }
  body { position: relative; font-family: "Source Sans 3", sans-serif; }

  .hero-band { position: absolute; left: 0; top: 5px; width: 1200px; height: 446px; background: var(--brand-blue); }

  .brand-box {
    position: absolute; left: 115px; top: 5px; width: 173px; height: 215px;
    background: var(--white); box-shadow: 0 8px 6px -4px rgba(0,0,0,0.35);
    display: flex; align-items: center; justify-content: center; gap: 8px;
  }
  .brand-square { width: 14px; height: 14px; background: var(--brand-blue); }
  .brand-name { font-size: 30px; font-weight: 700; color: var(--brand-blue); letter-spacing: -0.5px; }

  .main-nav { position: absolute; left: 114px; top: 250px; width: 175px; list-style: none; }
  .main-nav li {
    height: 27px; margin-bottom: 3px; background: var(--nav-grey);
    border-left: 8px solid var(--nav-stripe); padding-left: 10px;
    font-size: 15px; line-height: 27px; color: var(--text-dark);
  }
  .main-nav li.is-current { background: var(--white); border-left-color: var(--nav-grey); color: var(--brand-blue); }

  .hero-frame {
    position: absolute; left: 308px; top: 36px; width: 778px; height: 475px;
    background: var(--white); padding: 7px; border-bottom: 8px solid var(--frame-grey);
  }
  .hero-shadow {
    position: absolute; left: 318px; top: 511px; width: 758px; height: 22px;
    background: radial-gradient(ellipse at 50% 0%, rgba(0,0,0,0.22), rgba(0,0,0,0) 70%);
  }
  .hero-photo {
    width: 764px; height: 460px;
    background: linear-gradient(180deg, #eef2f5 0%, #dfe8ee 45%, #7fa7bd 62%, #3a3f46 75%, #1c1f24 100%);
  }

  .contact-panel {
    position: absolute; left: 0; top: 539px; width: 309px; height: 183px;
    background: var(--brand-blue); border-right: 6px solid var(--nav-grey);
    padding: 30px 0 0 45px; color: var(--white);
  }
  .contact-panel h2 { font-size: 25px; font-weight: 700; line-height: 34px; margin-bottom: 2px; }
  .contact-panel p { font-size: 17px; font-weight: 600; line-height: 25px; }

  .welcome { position: absolute; left: 360px; top: 553px; width: 720px; }
  .welcome h1 { font-size: 31px; font-weight: 700; color: var(--brand-blue); line-height: 40px; margin-bottom: 13px; }
  .welcome p { font-size: 15px; line-height: 23px; color: var(--text-body); }

  .site-footer {
    position: absolute; left: 0; top: 769px; width: 1200px; height: 43px;
    background: var(--footer-grey); text-align: center;
    font-size: 12px; line-height: 43px; color: var(--text-dark);
  }
</style>
</head>
<body>
  <div class="hero-band"></div>

  <div class="brand-box">
    <span class="brand-square"></span>
    <span class="brand-name">Corvalith</span>
  </div>

  <ul class="main-nav">
    <li class="is-current">Home</li>
    <li>About</li>
    <li>What we do</li>
    <li>People</li>
    <li>Ideas</li>
    <li>Contact us</li>
  </ul>

  <div class="hero-frame">
    <div class="hero-photo" role="img" aria-label="Three business people seated at a glossy meeting table in front of a bright window overlooking the sea"></div>
  </div>
  <div class="hero-shadow"></div>

  <section class="contact-panel">
    <h2>Contact us</h2>
    <p>miraholt@corvalith.com.au</p>
    <p>(02) 5550 1834</p>
    <p>PO Box XXX XXX Sydney Australia</p>
  </section>

  <section class="welcome">
    <h1>Welcome to Our Website</h1>
    <p>Corvalith is a media strategy, planning and buying agency.<br>
    We work with both small and big businesses.<br>
    Corvalith works across all offline platforms (radio, press, outdoor &amp; TV), search engine marketing, online display,<br>
    email, social &amp; mobile. We attain a high level of value for our clients with a focus on integration.<br>
    We are marketing partners in our clients businesses and enjoy seeing them grow and achieve their goals.</p>
  </section>

  <footer class="site-footer">©2013 Corvalith Media Group, All Rights Reserved.</footer>
</body>
</html>
```